Norwegian psychologist service needs a fresh and exiting web site*

Norwegian psychologist service: working with therapy, personal development, mastery and personal growth. Focus: children and teenagers with special needs; family dynamics; group processes; individuals with a need for therapy and personal growth. (Our company name: Fjordlys og samhold (means Mastery and Growth).

We already have a logo for the company, which will be used (will be attached in the project).

The webside is to be structured in 4 pages with roll down curtain menus (the numbers are just for guiding the designer - the should not be added):

Page 1: Om Fjordlys og Samhold (about Mastery and Growth): this is where our business is is presented/described shortly: Lorem Ipsum dolor cit...

Page 2: Tjenester (Services): this is where our 5 service areas are presented:
2.1 Utredning (Investigation, diagnosing): Lorem Ipsum dolor cit...
2.2 Rådgivning (consulting): Lorem Ipsum dolor cit...

2.3 Kurs og work shops (courses and work shops): Lorem Ipsum dolor cit...
2.3a Fjordlys og samhold Tema 1 (T1)
2.3b Fjordlys og samhold Tema 2 (T2)
2.3c Fjordlys og samhold Tema 3 (T3)

2.4 Terapi og utvikling (Therapy and development)
2.4a Fjordlys og samhold for individer (FS1)
2.4b Fjordlys og samhold i familier (FS2)
2.4c Fjordlys og samhold i grupper (FS3)
2.4d Fjordlys og samhold i institusjoner (FS4)

Page 3: Aktuelt (Blog): this is our blog where we share knowledge and articles

Page 4: Kontakt (Contact): This is the contact form page. Contact form should constitute:
- Ditt navn (your name)
- E-post (your e-mail)
- Emne (subject)
- Melding (message/description)

Our project should also include suggestion for handheld units (iPhone, iPad).
Updates

We have both been traveling with work for a while, and then unfortunately both of us got sick on return, so we need a few more days to evaluate and choose design. Kind Regards Arvid & Margit

Target Market(s)

Focus on therapy, learning, mastery and growth for children and teenagers with special needs, within the family dynamics, or in a group setting.
OUR MARKETS:
Private market: individuals, families, groups and health industry institutions (with focus on learning, mastery, growth (as well as growing up) and psychiatry for children and teenagers with special difficulties and needs)
Public institutions: Government institutions, state institutions and municipality institutions (e.g. schools, municipality health service, hospitals) that serve the public (families with children and teenagers with special needs, and where learning, mastery, growth (as well as growing up) and potential psychiatry is an issue).

Number of Pages Required

4 page

Font styles to use
Sans Serif

Colors

Designer to choose colors to be used in the design.

Requirements
Must have
• The website must have 4 pages with roll down curtain menus (we have added a PDF with suggested structure, and headings, with sub menus - see attached PDF drawing.
• The web page must also use the added logo file - and make the web page work well with our logo.
• We would like the website to have a modern look and we would like the site to be associated with typical HIGH END TOP QUALITY private health institutions, but with a stronger focus on human beings (hands, faces etc), and not white coats and doctors. We are psychologists in the private market.
• For instance, if photos are being used - we tend to like "warm" almost art-like, "grainy" two-tone (e.g. sepia) photos to illustrate our focus. If designer can find such photos as part of design, it would be interesting to us. We would like a few photos like that integrated in the design.
• We also want a design suggestion for how the web page should look like and behave on handheld units (e.g. iPhone, iPad).
Nice to have
• If designer could find a number of suitable photos that matches the business idea and design requirements (see description above), that could follow website, that would be good.
• It could also be nice to have graphic symbols that denote the different pages/subpages (subjects)....
• HORSES: we sometimes use horses as a "tool" in therapy sessions. The horse is not necessarily used for riding, but for contact, communication and grooming. PHOTOS: we would like the designer to find an opportunity for using a photo reflecting this cooperation between therapist, child, teenager and horse. It is a bit up to the designer to find a way to do this... Since the horse is only a tool, among many other tools, it does not have to be much - but we want to try and see how it will work with a photo that also reflects this part of our business.

```html
<!DOCTYPE html>
<html lang="no">
<head>
<meta charset="utf-8">
<title>Kontakt oss – Fjordlys og Samhold</title>
<link rel="stylesheet" href="https://fonts.googleapis.com/css2?family=Playfair+Display:wght@400;700;800&display=swap">
<style>
  :root {
    --navy: #2b3990;
    --green: #1cc774;
    --field-border: #d2d3e3;
    --header-shadow: #c9c9d2;
    --muted: #8a8a93;
    --white: #ffffff;
  }
  * { box-sizing: border-box; margin: 0; padding: 0; }
  html, body {
    width: 1116px;
    height: 1200px;
    overflow: hidden;
    background: var(--white);
    font-family: "Playfair Display", Georgia, serif;
    color: var(--navy);
  }
  .page { position: relative; width: 1116px; height: 1200px; }

  .site-header {
    position: absolute; left: 0; top: 0;
    width: 100%; height: 153px;
    border-bottom: 1px solid var(--header-shadow);
    box-shadow: 0 1px 2px rgba(0,0,0,0.08);
  }
  .nav-link {
    position: absolute; top: 63px;
    font-size: 12.5px; font-weight: 700;
    color: var(--navy); text-decoration: none;
    line-height: 18px;
  }
  .nav-about { left: 115px; }
  .nav-services { left: 311px; }
  .nav-chevron { position: absolute; left: 379px; top: 69px; }
  .nav-news { left: 735px; }
  .nav-contact { left: 846px; }
  .search-button {
    position: absolute; left: 959px; top: 52px;
    width: 42px; height: 42px;
    border: 1px solid var(--field-border); border-radius: 50%;
    display: flex; align-items: center; justify-content: center;
  }

  .brand {
    position: absolute; left: 458px; top: 40px;
    width: 200px; text-align: center;
  }
  .brand-mark {
    display: block; margin: 0 auto 8px;
    width: 30px; height: 30px; border-radius: 50%;
    background: var(--navy);
  }
  .brand-name {
    font-size: 17px; font-weight: 700; color: var(--navy);
    letter-spacing: 0.5px; white-space: nowrap;
  }

  .page-title {
    position: absolute; left: 0; top: 242px; width: 100%;
    text-align: center;
    font-size: 26px; font-weight: 700; letter-spacing: 0.3px;
    line-height: 32px;
  }
  .title-rule {
    position: absolute; top: 258px; width: 43px; height: 1.5px;
    background: var(--navy);
  }
  .title-rule-left { left: 378px; }
  .title-rule-right { left: 694px; }

  .field-label {
    position: absolute;
    font-size: 18.5px; font-weight: 700; line-height: 22px;
    letter-spacing: 0.2px;
  }
  .field {
    position: absolute;
    border: 1.5px solid var(--field-border); border-radius: 3px;
    background: var(--white);
  }
  .label-name { left: 221px; top: 345px; }
  .label-email { left: 570px; top: 345px; }
  .field-name { left: 221px; top: 390px; width: 325px; height: 50px; }
  .field-email { left: 570px; top: 390px; width: 325px; height: 50px; }
  .label-subject { left: 221px; top: 470px; }
  .field-subject { left: 221px; top: 515px; width: 674px; height: 51px; }
  .label-message { left: 220px; top: 596px; }
  .field-message { left: 221px; top: 641px; width: 674px; height: 232px; }

  .submit-button {
    position: absolute; left: 453px; top: 947px;
    width: 217px; height: 56px;
    background: var(--green); border: none; border-radius: 9px;
    color: var(--white);
    font-family: "Playfair Display", Georgia, serif;
    font-size: 19px; font-weight: 700;
  }

  .site-footer {
    position: absolute; left: 0; top: 1175px; width: 100%;
    text-align: center; font-size: 9.5px; color: var(--muted);
  }
</style>
</head>
<body>
<div class="page">
  <header class="site-header">
    <a class="nav-link nav-about" href="#">Om Fjordlys og Samhold</a>
    <a class="nav-link nav-services" href="#">Tjenester</a>
    <svg class="nav-chevron" width="11" height="7" viewBox="0 0 11 7" aria-hidden="true">
      <polyline points="0.5,0.5 5.5,6 10.5,0.5" fill="none" stroke="#2b3990" stroke-width="1"/>
    </svg>
    <div class="brand">
      <span class="brand-mark"></span>
      <span class="brand-name">Fjordlys og Samhold</span>
    </div>
    <a class="nav-link nav-news" href="#">Aktuelt</a>
    <a class="nav-link nav-contact" href="#">Kontakt</a>
    <div class="search-button" aria-label="Søk">
      <svg width="17" height="17" viewBox="0 0 17 17" aria-hidden="true">
        <circle cx="7" cy="7" r="5.8" fill="none" stroke="#2b3990" stroke-width="1.2"/>
        <line x1="11.2" y1="11.2" x2="16" y2="16" stroke="#2b3990" stroke-width="1.2"/>
      </svg>
    </div>
  </header>

  <main>
    <span class="title-rule title-rule-left"></span>
    <h1 class="page-title">KONTAKT OSS</h1>
    <span class="title-rule title-rule-right"></span>

    <form class="contact-form">
      <label class="field-label label-name">DITT NAVN</label>
      <div class="field field-name"></div>
      <label class="field-label label-email">E-POST</label>
      <div class="field field-email"></div>
      <label class="field-label label-subject">EMNE</label>
      <div class="field field-subject"></div>
      <label class="field-label label-message">MELDING</label>
      <div class="field field-message"></div>
      <button class="submit-button" type="button">SENDE</button>
    </form>
  </main>

  <footer class="site-footer">©2020 Fjordlys og Samhold. All Rights Reserved.</footer>
</div>
</body>
</html>
```